Holvik Cabinets Quality Custom Built Kitchens, Vanity Units, Robes ect

Hi,
Was after a new design for our business cards,
we are a cabinet making business and pride ourselves in quality custom built Kitchens, Vanity units, robes ect.
we have been around for over 20 years and we are trying to modernize our card logo.
Looking for something eye catching, bold and exciting
family ran and operated business, we work with builders and also have a large private clientel.

Thanks

Industry/Entity Type

Business

Contact Information for Business Card

Holvik Cabinets

Font styles to use
Serif
Script

Requirements
Must have
• Corinne 0461735928 hvcabinets@mailvane.com
• Po Box 2786
• 5B Wattlebark Court Marrowdale Vic 3851
• Phone (03)59286417 Fax (03) 59286942
Nice to have
• Quality Custom Built Kitchens & Vanity Units

```html
<!DOCTYPE html>
<html lang="en">
<head>
<meta charset="utf-8">
<title>Holvik Cabinets – Business Card</title>
<link rel="stylesheet" href="https://fonts.googleapis.com/css2?family=Montserrat:wght@700;800&family=Open+Sans:wght@400;600&display=swap">
<style>
  :root {
    --backdrop: #232428;
    --card: #ffffff;
    --maroon: #5e3f43;
    --ink: #231f20;
    --band-dark: #0d0d0d;
    --band-text: #ffffff;
  }
  * { margin: 0; padding: 0; box-sizing: border-box; }
  html, body { width: 1200px; height: 900px; overflow: hidden; }
  body {
    background: var(--backdrop);
    font-family: "Open Sans", Arial, sans-serif;
    position: relative;
  }
  .card {
    position: absolute;
    width: 525px;
    height: 300px;
    background: var(--card);
    overflow: hidden;
    box-shadow: 0 10px 28px rgba(0,0,0,.45);
  }
  .card--front { left: 50px; top: 300px; }
  .card--back { left: 625px; top: 300px; }

  .brand { position: absolute; }
  .card--front .brand { left: 0; right: 0; top: 112px; text-align: center; }
  .card--back .brand { left: 30px; top: 136px; }
  .brand__name {
    font-family: "Montserrat", Arial, sans-serif;
    font-weight: 800;
    color: var(--maroon);
    font-size: 34px;
    letter-spacing: .5px;
    line-height: 1;
    text-transform: uppercase;
    white-space: nowrap;
  }
  .brand__tagline {
    font-family: "Montserrat", Arial, sans-serif;
    font-weight: 700;
    color: var(--ink);
    font-size: 12px;
    margin-top: 8px;
    white-space: nowrap;
  }
  .card--back .brand__name { font-size: 22px; letter-spacing: .3px; }
  .card--back .brand__tagline { font-size: 8.3px; margin-top: 6px; }

  .holder {
    position: absolute;
    left: 300px; top: 60px;
    font-family: "Montserrat", Arial, sans-serif;
    font-weight: 800;
    font-size: 34px;
    color: var(--maroon);
  }
  .contacts {
    position: absolute;
    left: 300px; top: 116px;
    list-style: none;
    font-size: 13px;
    color: var(--ink);
    line-height: 19px;
  }
  .contacts li { display: flex; align-items: center; gap: 7px; }
  .contacts svg { width: 13px; height: 13px; flex: none; }

  .address-band { position: absolute; left: 0; bottom: 0; width: 100%; height: 34px; }
  .address-band svg { position: absolute; inset: 0; width: 100%; height: 100%; }
  .address-band__text {
    position: absolute;
    right: 16px; bottom: 0;
    height: 34px; line-height: 34px;
    color: var(--band-text);
    font-size: 12.5px;
    white-space: nowrap;
  }
</style>
</head>
<body>
  <section class="card card--front">
    <div class="brand">
      <div class="brand__name">Holvik Cabinets</div>
      <div class="brand__tagline">Quality Custom Built Kitchens &amp; Vanity Units</div>
    </div>
  </section>

  <section class="card card--back">
    <div class="brand">
      <div class="brand__name">Holvik Cabinets</div>
      <div class="brand__tagline">Quality Custom Built Kitchens &amp; Vanity Units</div>
    </div>

    <div class="holder">Corinne</div>

    <ul class="contacts">
      <li><svg viewBox="0 0 16 16" fill="none" stroke="#5e3f43" stroke-width="1.5"><rect x="4" y="1" width="8" height="14" rx="1.5"/><line x1="7" y1="12.5" x2="9" y2="12.5"/></svg>0461735928</li>
      <li><svg viewBox="0 0 16 16" fill="#5e3f43"><rect x="2" y="6" width="12" height="8" rx="1"/><rect x="4" y="2" width="7" height="5" fill="none" stroke="#5e3f43" stroke-width="1.3"/></svg>(03) 59286942</li>
      <li><svg viewBox="0 0 16 16" fill="#5e3f43"><path d="M3 1.5l2.5 0 1.2 3.3-1.6 1.2a8 8 0 0 0 4.9 4.9l1.2-1.6 3.3 1.2 0 2.5c0 .8-.7 1.5-1.5 1.5A12 12 0 0 1 1.5 3c0-.8.7-1.5 1.5-1.5z"/></svg>(03)59286417</li>
      <li><svg viewBox="0 0 16 16" fill="none" stroke="#5e3f43" stroke-width="1.4"><rect x="1.5" y="3.5" width="13" height="9"/><polyline points="1.5,3.5 8,9 14.5,3.5"/></svg>hvcabinets@mailvane.com</li>
    </ul>

    <div class="address-band">
      <svg viewBox="0 0 525 34" preserveAspectRatio="none" aria-hidden="true">
        <rect x="0" y="0" width="525" height="34" fill="#5e3f43"/>
        <polygon points="232,0 525,0 525,34 214,34" fill="#0d0d0d"/>
      </svg>
      <div class="address-band__text">Po Box 2786 5B Wattlebark Court Marrowdale Vic 3851</div>
    </div>
  </section>
</body>
</html>
```